High-end construction company needs a business card design

We need a modern looking business card that draws people in, is memorable and looks so good people will want to sick it on their fridges.
On the first side what is needed are:
Logo
My name - Tomas Verbelk
Title - Managing Director
Website - www.kravel.co.uk
Email - tomas@kravel.co.uk
Telephone - 020 5194 6381
Mobile - 07845319027
On the back side was is needed is a list of all the services we provide:
-Kitchen Renovations
-Bathroom Renovations
-House Renovations
-Garage Conversions
-Extensions
-Loft Conversions
-Conservatories
-Carpentry
-Tiling
-Electrical
-Plumbing & Heating
-Bricklaying
-Landscaping
-Decorating
-Plastering
We would like the colours to be the same shades as on the logo with grey or black for the words.
Target Market(s)
Anyone who needs building work done
Contact Information for Business Card
This business card is for a construction company which strives to deliver excellent service and quality.
The look and feel of the card should represent this.
Requirements
Must have
- On the first side what is needed are:
Logo
My name - Tomas Verbelk
Title - Managing Director
Website - www.kravel.co.uk
Email - tomas@kravel.co.uk
Telephone - 020 5194 6381
Mobile - 07845319027
Nice to have
- Cool looking features

```html
<!DOCTYPE html>
<html lang="en">
<head>
<meta charset="utf-8">
<title>Kravel Construction Ltd – Business Card</title>
<link href="https://fonts.googleapis.com/css2?family=Arimo:wght@700&family=Nunito:wght@600&family=Open+Sans:wght@400;600&family=Montserrat:wght@800&display=swap" rel="stylesheet">
<style>
  :root {
    --page: #eef2ec;
    --card: #e6e7e8;
    --card-edge: #3a3a3c;
    --dark: #333234;
    --band-1: #8d8e90;
    --band-2: #aeafb1;
    --band-3: #cfd0d2;
    --ink: #333333;
    --green: #6dbb45;
    --logo-grey: #8a8a8c;
    --logo-white: #ffffff;
  }
  * { box-sizing: border-box; margin: 0; padding: 0; }
  html, body { width: 1200px; height: 1200px; overflow: hidden; }
  body { background: var(--page); position: relative; }

  .card {
    position: absolute;
    left: 250px;
    width: 700px;
    height: 400px;
    border-radius: 22px;
    border: 1px solid var(--card-edge);
    background: var(--card);
    overflow: hidden;
  }
  .card--front { top: 190px; }
  .card--back { top: 610px; }

  .front-swoosh { position: absolute; inset: 0; width: 700px; height: 400px; }

  .wordmark { position: absolute; text-align: center; font-family: "Montserrat", sans-serif; font-weight: 800; line-height: 1; }
  .wordmark--front { left: 40px; top: 100px; width: 190px; color: var(--logo-grey); }
  .wordmark--front .wordmark-name { font-size: 44px; letter-spacing: 1px; }
  .wordmark--front .wordmark-sub { font-size: 10.5px; letter-spacing: 1.6px; margin-top: 4px; }
  .wordmark--back { left: 200px; top: 130px; width: 300px; color: var(--logo-white); }
  .wordmark--back .wordmark-name { font-size: 76px; letter-spacing: 2px; }
  .wordmark--back .wordmark-sub { font-size: 18.5px; letter-spacing: 2.6px; margin-top: 6px; }

  .holder-name {
    position: absolute; left: 475px; top: 62px;
    font-family: "Arimo", sans-serif; font-weight: 700; font-size: 26px; color: var(--ink);
  }
  .holder-title {
    position: absolute; left: 475px; top: 102px;
    font-family: "Nunito", sans-serif; font-weight: 600; font-size: 17px; color: var(--green);
  }

  .contact-list { position: absolute; left: 280px; top: 218px; list-style: none; }
  .contact-item { display: flex; align-items: center; height: 24px; margin-bottom: 14px; }
  .contact-item:nth-child(3) { margin-bottom: 18px; }
  .contact-icon { width: 24px; height: 24px; margin-right: 22px; flex: none; }
  .contact-text { font-family: "Arimo", sans-serif; font-weight: 700; font-size: 20px; color: var(--green); }

  .services { position: absolute; left: 0; top: 232px; width: 700px; text-align: center; font-family: "Open Sans", sans-serif; }
  .services-heading {
    font-weight: 600; font-size: 16px; color: var(--green);
    text-decoration: underline; text-underline-offset: 3px; margin-bottom: 3px;
  }
  .services-line { font-size: 14.5px; color: var(--ink); line-height: 20.5px; }
</style>
</head>
<body>

<section class="card card--front">
  <svg class="front-swoosh" viewBox="0 0 700 400" aria-hidden="true">
    <path fill="var(--band-3)" d="M0,0 H458 C330,60 235,210 232,400 H0Z"/>
    <path fill="var(--band-2)" d="M0,0 H456 C320,60 220,210 215,400 H0Z"/>
    <path fill="var(--band-1)" d="M0,0 H454 C310,60 205,210 200,400 H0Z"/>
    <path fill="var(--dark)" d="M0,0 H452 C300,60 190,210 185,400 H0Z"/>
  </svg>

  <div class="wordmark wordmark--front">
    <div class="wordmark-name">KRAVEL</div>
    <div class="wordmark-sub">CONSTRUCTION LTD</div>
  </div>

  <h1 class="holder-name">Tomas Verbelk</h1>
  <p class="holder-title">Managing Director</p>

  <ul class="contact-list">
    <li class="contact-item">
      <svg class="contact-icon" viewBox="0 0 24 24" aria-label="Mobile">
        <circle cx="12" cy="12" r="11" fill="var(--green)"/>
        <path d="M8 6.5 L10 6 L11 9 L9.8 10 C10.5 11.8 12 13.4 13.8 14.2 L14.8 13 L17.6 14 L17.2 16.2 C12 16.5 7.5 12 8 6.5Z" fill="#4a4a4a"/>
      </svg>
      <span class="contact-text">07845319027</span>
    </li>
    <li class="contact-item">
      <svg class="contact-icon" viewBox="0 0 24 24" aria-label="Telephone">
        <circle cx="12" cy="12" r="11" fill="var(--green)"/>
        <path d="M6 9 Q12 5 18 9 L17 10.5 L15 10 L15 9 Q12 8 9 9 L9 10 L7 10.5Z" fill="#4a4a4a"/>
        <rect x="8" y="11" width="8" height="6" rx="1" fill="#4a4a4a"/>
      </svg>
      <span class="contact-text">020 5194 6381</span>
    </li>
    <li class="contact-item">
      <svg class="contact-icon" viewBox="0 0 24 24" aria-label="Email">
        <circle cx="12" cy="12" r="11" fill="var(--green)"/>
        <rect x="6.5" y="8" width="11" height="8" fill="#4a4a4a"/>
        <path d="M6.5 8 L12 12.5 L17.5 8" fill="none" stroke="#d9d9d9" stroke-width="1"/>
      </svg>
      <span class="contact-text">tomas@kravel.co.uk</span>
    </li>
    <li class="contact-item">
      <svg class="contact-icon" viewBox="0 0 24 24" aria-label="Website">
        <circle cx="12" cy="12" r="11" fill="var(--green)"/>
        <g fill="none" stroke="#4a4a4a" stroke-width="1.2">
          <circle cx="12" cy="12" r="6"/>
          <ellipse cx="12" cy="12" rx="2.6" ry="6"/>
          <path d="M6 12 H18 M7 9 H17 M7 15 H17"/>
        </g>
      </svg>
      <span class="contact-text">www.kravel.co.uk</span>
    </li>
  </ul>
</section>

<section class="card card--back">
  <div class="wordmark wordmark--back">
    <div class="wordmark-name">KRAVEL</div>
    <div class="wordmark-sub">CONSTRUCTION LTD</div>
  </div>

  <div class="services">
    <h2 class="services-heading">Services</h2>
    <p class="services-line">• Kitchen Renovations • Bathroom Renovations • House Renovations</p>
    <p class="services-line">• Garage Conversions &nbsp;• Extensions • Loft Conversions</p>
    <p class="services-line">• Conservatories • Carpentry • Tiling • Electrical • Plumbing &amp; Heating</p>
    <p class="services-line">• Bricklaying • Landscaping • Decorating • Plastering</p>
  </div>
</section>

</body>
</html>
```